VELMORAIR Business Card

We need a new elegant business card.
We are a company of business jet.
In attachment the old business card (2 sides) and the new logo.

Our adress is :
Aéroport de Brévillac la Combe - Bât.206
64390 TOUSSUS LE NOBLE - FRANCE

Target Market(s)

Lux

Industry/Entity Type

Business

Contact Information for Business Card

You can see the example in attachment

Font styles to use
Serif
Sans Serif

Requirements
Must have
• The color of the logo (white, black, blue)

```html
<!DOCTYPE html>
<html lang="en">
<head>
<meta charset="utf-8">
<title>VELMORAIR Business Card</title>
<link rel="stylesheet" href="https://fonts.googleapis.com/css2?family=Montserrat:wght@400;500;600&family=Open+Sans:wght@600&display=swap">
<style>
  :root {
    --backdrop: #d9d9d9;
    --card: #0b0b0b;
    --card-edge: #1a1a1a;
    --blue: #1fb4ea;
    --white: #ffffff;
    --silver: #bdbdbd;
    --rule: #2a2a2a;
  }
  * { box-sizing: border-box; margin: 0; padding: 0; }
  html, body { width: 1200px; height: 900px; overflow: hidden; }
  body {
    background: var(--backdrop);
    font-family: "Montserrat", Arial, sans-serif;
    position: relative;
  }
  .card {
    position: absolute;
    left: 320px;
    width: 560px;
    height: 320px;
    background: radial-gradient(ellipse at 40% 30%, var(--card-edge), var(--card) 70%);
    box-shadow: 0 10px 24px rgba(0,0,0,.25);
  }
  .card--front { top: 80px; }
  .card--back { top: 480px; }

  /* front side */
  .front-brand {
    position: absolute;
    top: 78px; left: 0; right: 0;
    text-align: center;
    color: var(--white);
    font-weight: 600;
    font-size: 40px;
    letter-spacing: 2px;
  }
  .front-brand .brand-dot {
    display: inline-block;
    width: 22px; height: 22px;
    border-radius: 50%;
    background: var(--blue);
    margin-left: 10px;
    vertical-align: 2px;
  }
  .front-info {
    position: absolute;
    top: 170px; left: 0; right: 0;
    text-align: center;
    font-family: "Open Sans", Arial, sans-serif;
    font-weight: 600;
    color: var(--blue);
    font-size: 16px;
    line-height: 25px;
  }
  .front-info .cities { margin-top: 14px; }

  /* back side */
  .holder {
    position: absolute;
    top: 106px; left: 34px;
  }
  .holder-name {
    color: var(--blue);
    font-weight: 500;
    font-size: 25px;
    letter-spacing: .3px;
  }
  .holder-role {
    color: var(--white);
    font-size: 14px;
    margin-top: 2px;
  }
  .divider {
    position: absolute;
    top: 172px; left: 34px; right: 40px;
    height: 1px;
    background: var(--rule);
  }
  .back-brand {
    position: absolute;
    top: 64px; right: 40px;
    display: flex; align-items: center; gap: 12px;
    color: var(--blue);
    font-weight: 600;
    font-size: 22px;
    letter-spacing: 1px;
  }
  .back-brand .brand-dot {
    width: 54px; height: 54px;
    border-radius: 50%;
    background: var(--blue);
  }
  .contacts {
    position: absolute;
    right: 36px; top: 190px;
    list-style: none;
    color: var(--white);
    font-size: 15px;
    line-height: 24px;
    text-align: right;
  }
  .contacts li { display: flex; justify-content: flex-end; align-items: center; gap: 10px; }
  .contacts svg { width: 12px; height: 12px; fill: none; stroke: var(--blue); stroke-width: 1.6; }
</style>
</head>
<body>
  <section class="card card--front">
    <div class="front-brand">VELMORAIR<span class="brand-dot"></span></div>
    <div class="front-info">
      <p>Book your private jet online</p>
      <p>www.velmorair.com</p>
      <p class="cities">Paris - London - Lyon - Geneva - Cannes</p>
    </div>
  </section>

  <section class="card card--back">
    <div class="holder">
      <p class="holder-name">Julien Marchal</p>
      <p class="holder-role">Managing Director</p>
    </div>
    <div class="back-brand"><span class="brand-dot"></span>VELMORAIR</div>
    <div class="divider"></div>
    <ul class="contacts">
      <li>123.456.7890
        <svg viewBox="0 0 12 12"><rect x="3" y="1" width="6" height="10" rx="1"/></svg></li>
      <li>123.456.7890
        <svg viewBox="0 0 12 12"><path d="M2 4 Q6 0 10 4 L9 5 L7 4 L5 4 L3 5 Z M3 6 H9 V10 H3 Z"/></svg></li>
      <li>info@youremail.com
        <svg viewBox="0 0 12 12"><rect x="1" y="3" width="10" height="7"/><path d="M1 3 L6 7 L11 3"/></svg></li>
      <li>www.website.com
        <svg viewBox="0 0 12 12"><path d="M5 7 L7 5 M4 6 L2 8 Q2 10 4 10 L6 8 M8 6 L10 4 Q10 2 8 2 L6 4"/></svg></li>
    </ul>
  </section>
</body>
</html>
```